Thank you for exploring whether you are interested in creating a book cover for the Insight Lantern!

The cover should look professional yet appeal to a person who is open to approaching life more deeply.

The logo that I've uploaded is something that you are welcome to use in your book cover design but is not required to be the primary graphic.

The following is a description of the Insight Lantern and its purpose.
RADICAL CLARITY IS POSSIBLE

Are you tired of hitting up against your limitations? Do you wish you could be more effective in everything you do? What would it be like if you could walk confidently into any situation and automatically comprehend it, organize your thoughts, and respond creatively? This kind of radical clarity is not only possible, it’s right in front of you—and The Insight Lantern: Notice What Matters. Hold Bold Dialogues. Build the Days You Crave. shows you the pathway to get there!

In the book, Dr. Lorne Haskett draws on over 30 years of experience with executive coaching and leadership development to deliver priceless wisdom about how to see clearly in today’s complex and uncertain world. Using his Insight Lantern, you’ll discover where you’re stuck and why, find your authentic direction, and learn to engage creatively with life so you can start getting what you really want.

A TRANSFORMATIONAL TOOL

The Insight Lantern is a cutting-edge leadership development tool that supports you to activate your maximum potential, both personally and professionally. It’s based on the idea that there are four fundamental building blocks to reality: Intentions, Actions, Facts, and Stories. Understanding the differences between these dimensions of your experience and learning how they work together is the key to forging a clear path toward your destination in life. The Insight Lantern organizes these four main building blocks around the two polarities of a compass:

1. North to South – Intentions to Actions
We all have billions of intentions, but how many do we actually put into action? In this polarity you learn to notice and implement your intentions in order to generate more effective actions and create meaningful outcomes in your life.

2. East vs. West – Facts vs. Stories
We all create stories to make sense of life, but how many of us actually get clear on the facts to see where our stories might be off? In this polarity you learn to discern the objective facts from your subjective interpretations and stories, illuminating a clearer perspective to uncover what’s been blocking you on the path to success.

Using the Insight Lantern you’ll discover how naming and implementing your intentions in life naturally results in more effective behavior and actions, and how distinguishing the real facts from your interpretations of any situation can propel you toward radical clarity and true fulfillment.

BOLD DIALOGUES

The key benefit of using the Insight Lantern is that you’ll have more of what Lorne calls “Bold Dialogues.” Bold dialogues are those that move you closer to what you’re wanting in life—the kind of human-to-human interactions that actually make a difference. By applying the Insight Lantern, you gain critical insight that opens your eyes to new opportunities for Bold Dialogues, helping you draw on your imagination and move beyond your current stance toward a positive outcome. Every conversation is a possibility waiting to be discovered. The more Bold Dialogues you have, the more profound and meaningful shifts you activate in your life.

PRACTICAL GUIDANCE

The book doesn’t just give you a theoretical understanding of how to gain more clarity in your life. Dr. Haskett provides you with clear, practical steps to develop the core competencies you need to start getting the results you want. As you explore the book, you’ll find:

• A thorough description of all the directions of the Insight Lantern, each with three main points to focus your energy on.
• Case studies from Lorne’s many clients who have successfully used the Insight Lantern to transform their own lives.
• Hands-on practices Lorne has developed to help you put your new skills to use immediately.
• Step-by-step guidance to apply the Insight Lantern in any situation, including real-life stories from people who have experienced genuine transformation using this tool.

The Insight Lantern will help you to deepen your understanding of the challenges in your life, integrate new competencies to boost your effectiveness, and awaken to exciting opportunities for your own growth, leadership, and success!

ABOUT THE AUTHOR

Dr. Lorne Haskett has over 30 years of experience with leadership development and executive coaching work. As owner and principal coach of Haskett Leadership Consultants, he has been integrating the fields of management consulting, business psychology, and leadership coaching since 1983. Lorne holds a Ph.D. in psychodynamic and group psychology from the Merrowind Graduate Institute, an M.A. in human growth and potential from the University of Fallbrook Ridge, and a B.A. in accounting and Business Administration from Kestrel Vale University. He is the creator of the Insight Lantern™, a leadership development tool that supports people to see life clearly, wake up to exciting opportunities for their own growth and leadership, and take empowered action toward true success. Lorne’s combination of business expertise, human compassion, and incisive questions help his clients achieve unprecedented results.

Target Market(s)

Out intended audience is folks who would like to be more effective and to grow and transform. This being more productive and developing could be in their careers or their personal lives.

Industry/Entity Type

It Professional

Requirements
Must have
• Stock images, if used, that I can purchase exclusively or that you can easily create specifically for the book once you are the chosen designer. I completely understand using stock imaging in your submissions pre-selection.
Nice to have
• Ideally the cover will include both the title and subtitle.

```html
<!DOCTYPE html>
<html lang="en">
<head>
<meta charset="utf-8">
<title>The Insight Lantern – Book Cover Spread</title>
<link rel="stylesheet" href="https://fonts.googleapis.com/css2?family=Cinzel:wght@400;500&family=Tinos:ital,wght@0,400;0,700&display=swap">
<style>
  :root {
    --page: #ffffff;
    --cover-light: #ffffff;
    --cover-edge: #d9d9d9;
    --ink: #1c1c1c;
    --teal: #1e5f78;
    --orange: #f6a21c;
    --rule: #222222;
  }
  * { margin: 0; padding: 0; box-sizing: border-box; }
  html, body { width: 1200px; height: 1200px; overflow: hidden; background: var(--page); }
  .canvas { position: relative; width: 1200px; height: 1200px; }

  .spread {
    position: absolute; left: 10px; top: 194px; width: 1180px; height: 818px;
    background: radial-gradient(ellipse at 50% 50%, var(--cover-light) 45%, var(--cover-edge) 100%);
  }

  /* Back cover */
  .back-copy {
    position: absolute; left: 31px; width: 512px;
    font-family: "Tinos", "Times New Roman", serif;
    font-size: 11.4px; line-height: 15.4px; color: var(--ink); text-align: justify;
  }
  .back-copy p + p { margin-top: 15px; }
  .back-copy ul { margin: 10px 0 10px 32px; }
  .back-copy li { margin-bottom: 2px; }
  .copy-intro { top: 70px; }
  .copy-practical { top: 277px; }
  .copy-author { top: 572px; }
  .copy-author strong { font-weight: 700; }

  /* Spine */
  .spine-text {
    position: absolute; left: 585px;
    font-family: "Cinzel", "Times New Roman", serif;
    font-size: 25px; letter-spacing: 2.5px; color: var(--ink);
    writing-mode: vertical-rl; white-space: nowrap;
  }
  .spine-title { top: 50px; }
  .spine-author { top: 481px; }
  .spine-mark {
    position: absolute; left: 563px; top: 405px; width: 44px; height: 44px;
    border-radius: 50%; background: var(--teal); border: 3px solid var(--orange);
  }

  /* Front cover */
  .front { position: absolute; left: 615px; top: 0; width: 565px; height: 818px; }
  .front-kicker {
    position: absolute; top: 60px; left: 0; width: 100%;
    display: flex; justify-content: center; align-items: center; gap: 14px;
    font-family: "Cinzel", serif; font-size: 24px; letter-spacing: 6px; color: var(--ink);
  }
  .front-kicker .rule { width: 84px; height: 2px; background: var(--rule); }
  .title-line {
    position: absolute; left: 0; width: 100%; text-align: center;
    font-family: "Cinzel", "Times New Roman", serif; font-weight: 400;
    font-size: 92px; line-height: 1; letter-spacing: 1px;
  }
  .title-insight { top: 100px; color: var(--teal); }
  .title-lantern { top: 180px; color: var(--orange); }
  .subtitle {
    position: absolute; top: 292px; left: 0; width: 100%; text-align: center;
    font-family: "Cinzel", "Times New Roman", serif; font-size: 16px;
    line-height: 25px; letter-spacing: 3px; color: var(--ink);
  }
  .brand-mark {
    position: absolute; top: 460px; left: 0; width: 100%;
    display: flex; flex-direction: column; align-items: center; gap: 16px;
  }
  .brand-mark .dot {
    width: 120px; height: 120px; border-radius: 50%;
    background: var(--teal); border: 6px solid var(--orange);
  }
  .brand-mark .name {
    font-family: "Cinzel", serif; font-size: 18px; letter-spacing: 3px; color: var(--teal);
  }
  .front-author {
    position: absolute; top: 760px; left: 0; width: 100%; text-align: center;
    font-family: "Cinzel", "Times New Roman", serif; font-size: 25px;
    letter-spacing: 4px; color: var(--ink);
  }
</style>
</head>
<body>
<div class="canvas">
  <section class="spread">

    <div class="back-copy copy-intro">
      <p>Are you tired of hitting up against your limitations? Do you wish you could be more effective in everything you do? What would it be like if you could walk confidently into any situation and automatically comprehend it, organize your thoughts, and respond creatively? This kind of radical clarity is not only possible, it’s right in front of you—and The Insight Lantern: Notice What Matters. Hold Bold Dialogues. Build the Days You Crave. shows you the pathway to get there!</p>
      <p>In the book, Dr. Lorne Haskett draws on over 30 years of experience with executive coaching and leadership development to deliver priceless wisdom about how to see clearly in today’s complex and uncertain world. Using his Insight Lantern, you’ll discover where you’re stuck and why, find your authentic direction, and learn to engage creatively with life so you can start getting what you really want.</p>
    </div>

    <div class="back-copy copy-practical">
      <p>The book doesn’t just give you a theoretical understanding of how to gain more clarity in your life. Dr. Haskett provides you with clear, practical steps to develop the core competencies you need to start getting the results you want. As you explore the book, you’ll find:</p>
      <ul>
        <li>A thorough description of all the directions of the Insight Lantern, each with three main points to focus your energy on.</li>
        <li>Case studies from Lorne’s many clients who have successfully used the Insight Lantern to transform their own lives.</li>
        <li>Hands-on practices Lorne has developed to help you put your new skills to use immediately.</li>
        <li>Step-by-step guidance to apply the Insight Lantern in any situation, including real-life stories from people who have experienced genuine transformation using this tool.</li>
      </ul>
      <p>The Insight Lantern will help you to deepen your understanding of the challenges in your life, integrate new competencies to boost your effectiveness, and awaken to exciting opportunities for your own growth, leadership, and success!</p>
    </div>

    <div class="back-copy copy-author">
      <p><strong>Dr. Lorne Haskett</strong> has over 30 years of experience with leadership development and executive coaching work. As owner and principal coach of Haskett Leadership Consultants, he has been integrating the fields of management consulting, business psychology, and leadership coaching since 1983. Lorne holds a Ph.D. in psychodynamic and group psychology from the Merrowind Graduate Institute, an M.A. in human growth and potential from the University of Fallbrook Ridge, and a B.A. in accounting and Business Administration from Kestrel Vale University. He is the creator of the Insight Lantern™, a leadership development tool that supports people to see life clearly, wake up to exciting opportunities for their own growth and leadership, and take empowered action toward true success. Lorne’s combination of business expertise, human compassion, and incisive questions help his clients achieve unprecedented results.</p>
    </div>

    <div class="spine-text spine-title">THE INSIGHT LANTERN</div>
    <div class="spine-mark" aria-hidden="true"></div>
    <div class="spine-text spine-author">DR. LORNE HASKETT</div>

    <div class="front">
      <div class="front-kicker"><span class="rule"></span><span>THE</span><span class="rule"></span></div>
      <h1 class="title-line title-insight">INSIGHT</h1>
      <div class="title-line title-lantern">LANTERN</div>
      <p class="subtitle">Notice What Matters.<br>Hold Bold Dialogues.<br>Build the Days You Crave.</p>
      <div class="brand-mark">
        <span class="dot" aria-hidden="true"></span>
        <span class="name">Insight Lantern</span>
      </div>
      <div class="front-author">DR. LORNE HASKETT</div>
    </div>

  </section>
</div>
</body>
</html>
```